Pizza Box 10" x 10" - color: White

Custom design, utilizing CrustLoomo Logo and include the following information on the Pizza Box:

1. Custom Crafted Pizza with Quality Ingredients.
2. [....Get Your GAME ON] to be placed on the front flap and seen when the
box is opened.
3. You"ll miss 100% of the Pizza you don't eat.

4. Visit www.fennelcartonworks.example for additional design resource information. Go to site and then click on ORDERING to access.

5. The 10" x 10" Pizza Box is to be in the color WHITE.
6. Use colors Black and Red. no generic images. no food pics. I am looking for a clean and cool design.

Target Market(s)

Age 16 - 36 years

Industry/Entity Type

American Restaurant

Font styles to use
Sans Serif

Colors
ec1f27
000000
ffffff

Requirements
Must have
• Color Red and Black.
• Logo on Top and all sides of the Pizza Box.
Nice to have
• A Creative design that does not look generic.
Should not have
• No food images.

```html
<!DOCTYPE html>
<html lang="en">
<head>
<meta charset="utf-8">
<title>CrustLoomo 10 inch Pizza Box – Dieline</title>
<link rel="stylesheet" href="https://fonts.googleapis.com/css2?family=Montserrat:wght@700;800&family=Source+Sans+3:wght@300&display=swap">
<style>
  :root {
    --brand-red: #ec1f27;
    --brand-black: #000000;
    --paper: #ffffff;
    --cut-line: #4a4a4a;
    --print-guide: #ec1f27;
  }
  html, body {
    margin: 0;
    padding: 0;
    width: 1200px;
    height: 2400px;
    overflow: hidden;
    background: var(--paper);
  }
  .dieline-sheet {
    display: block;
    width: 1200px;
    height: 2400px;
  }
  .spec-heading {
    font-family: "Source Sans 3", sans-serif;
    font-weight: 300;
    font-size: 33px;
    fill: var(--brand-black);
  }
  .cut { fill: none; stroke: var(--cut-line); stroke-width: 1; }
  .fold { fill: none; stroke: var(--cut-line); stroke-width: 1; stroke-dasharray: 4 3; }
  .print-area { fill: none; stroke: var(--print-guide); stroke-width: 0.8; }
  .ink-black { fill: var(--brand-black); }
  .ink-red { fill: var(--brand-red); }
  .brand-name {
    font-family: "Montserrat", sans-serif;
    font-weight: 800;
    fill: var(--brand-black);
  }
  .brand-name--light { fill: var(--paper); }
  .copy-bold {
    font-family: "Montserrat", sans-serif;
    font-weight: 800;
    fill: var(--brand-black);
  }
  .copy-white { fill: var(--paper); }
  .copy-small {
    font-family: "Montserrat", sans-serif;
    font-weight: 700;
    fill: var(--paper);
  }
  .size-mark {
    font-family: "Montserrat", sans-serif;
    font-weight: 800;
    font-size: 28px;
    fill: var(--brand-black);
  }
  .brand-dot { fill: none; stroke: var(--brand-black); stroke-width: 2; }
</style>
</head>
<body>
<svg class="dieline-sheet" viewBox="0 0 750 1500" xmlns="http://www.w3.org/2000/svg">

  <!-- Specification heading -->
  <g class="spec-block">
    <text class="spec-heading" x="105" y="110">10″ Box  (printable areas)</text>
    <text class="spec-heading" x="105" y="157">Top - 9″ x 9″</text>
    <text class="spec-heading" x="105" y="204">Sides - 9″ x 1″</text>
    <text class="spec-heading" x="105" y="251">Flaps - 9″ x .75″</text>
  </g>

  <!-- Cut outline -->
  <g class="cut-lines">
    <!-- tuck flap -->
    <path class="cut" d="M185,395 V320 H232 L242,310 H455 L465,318 H565 V395"/>
    <path class="cut" d="M360,385 a15,15 0 1,0 30,0 a15,15 0 1,0 -30,0"/>
    <!-- upper corner pieces -->
    <path class="cut" d="M180,395 V378 a7,7 0 0,1 0,-14 V318 H105 V965"/>
    <path class="cut" d="M570,395 V378 a7,7 0 0,0 0,-14 V318 H645 V965"/>
    <path class="cut" d="M105,483 H180 M570,483 H645"/>
    <!-- lid front panel bottom edge with tabs -->
    <path class="cut" d="M180,480 H200 M550,480 H570"/>
    <path class="cut" d="M200,480 H240 V488 H300 V480 H450 V488 H510 V480 H550"/>
    <!-- lid/back seam -->
    <path class="cut" d="M105,875 H180 M570,875 H645"/>
    <!-- back wall lower edge -->
    <path class="cut" d="M180,875 V940 L195,955 H240 L250,945 H500 L510,955 H555 L570,940 V875"/>
    <path class="cut" d="M105,965 L185,955 M565,955 L645,965"/>
    <!-- base outer sides -->
    <path class="cut" d="M105,965 V1080 L120,1095 V1225 L105,1240 V1318 L185,1340"/>
    <path class="cut" d="M645,965 V1080 L630,1095 V1225 L645,1240 V1318 L565,1340"/>
    <path class="cut" d="M175,1165 H185 V1210 H175 M575,1165 H565 V1210 H575"/>
    <!-- front wall and tuck -->
    <path class="cut" d="M185,1340 V1395 L198,1440 H552 L565,1395 V1340"/>
    <path class="cut" d="M185,1340 H195 M555,1340 H565"/>
  </g>

  <!-- Fold lines -->
  <g class="fold-lines">
    <path class="fold" d="M185,390 H565"/>
    <path class="fold" d="M180,483 V875 M570,483 V875"/>
    <path class="fold" d="M180,480 H570"/>
    <path class="fold" d="M185,955 V1340 M565,955 V1340"/>
    <path class="fold" d="M185,1340 H565"/>
  </g>

  <!-- Lid front panel: slogan band -->
  <g class="lid-slogan">
    <rect class="ink-black" x="203" y="427" width="343" height="37"/>
    <text class="copy-bold copy-white" font-size="10.5" text-anchor="middle"
          transform="translate(375,445.5) rotate(180)" dominant-baseline="middle">You"ll miss 100% of the Pizza you don't eat.</text>
  </g>

  <!-- Lid side flaps -->
  <g class="lid-side lid-side--left">
    <rect class="print-area" x="123" y="505" width="40" height="345"/>
    <path class="ink-black" d="M123,505 H163 V545 L123,590 Z"/>
    <path class="ink-black" d="M123,850 H163 V765 L123,810 Z"/>
    <g transform="translate(143,680) rotate(90)">
      <circle class="brand-dot" cx="-55" cy="0" r="8"/>
      <text class="brand-name" x="8" y="0" font-size="15" text-anchor="middle" dominant-baseline="middle">CrustLoomo</text>
    </g>
  </g>
  <g class="lid-side lid-side--right">
    <rect class="print-area" x="587" y="505" width="40" height="345"/>
    <path class="ink-black" d="M587,505 H627 V590 L587,545 Z"/>
    <path class="ink-black" d="M587,850 H627 V810 L587,765 Z"/>
    <g transform="translate(607,660) rotate(-90)">
      <circle class="brand-dot" cx="-55" cy="0" r="8"/>
      <text class="brand-name" x="8" y="0" font-size="15" text-anchor="middle" dominant-baseline="middle">CrustLoomo</text>
    </g>
  </g>

  <!-- Back wall -->
  <g class="back-wall">
    <rect class="print-area" x="203" y="893" width="343" height="37"/>
    <g transform="translate(375,912) rotate(180)">
      <circle class="brand-dot" cx="-48" cy="0" r="7"/>
      <text class="brand-name" x="8" y="0" font-size="13" text-anchor="middle" dominant-baseline="middle">CrustLoomo</text>
    </g>
    <text class="size-mark" x="612" y="922" text-anchor="middle" dominant-baseline="middle">10</text>
  </g>

  <!-- Base panel artwork -->
  <g class="base-art">
    <rect class="print-area" x="203" y="973" width="343" height="345"/>
    <path class="ink-red" role="img" aria-label="Red field with abstract black pizza slice shapes and white curved stripes"
          d="M203,1318 V1180 Q380,1130 546,1082 V1318 Z"/>
    <circle class="brand-dot" cx="281" cy="1105" r="15"/>
    <text class="brand-name" x="310" y="1106" font-size="30" dominant-baseline="middle">CrustLoomo</text>
    <g transform="translate(332,1162) rotate(-12)">
      <text class="copy-bold copy-white" x="0" y="0" font-size="12">Get Your GAME ON</text>
      <text class="copy-small" x="0" y="12" font-size="6.5">Custom Crafted Pizza with Quality Ingredients.</text>
      <text class="copy-small" x="0" y="21" font-size="6.5">You"ll miss 100% of the Pizza you don't eat.</text>
    </g>
  </g>

  <!-- Base side walls -->
  <g class="base-side base-side--left">
    <rect class="print-area" x="136" y="975" width="29" height="343"/>
    <text class="copy-bold" font-size="10.5" text-anchor="middle" dominant-baseline="middle"
          transform="translate(150.5,1146) rotate(90)">Custom Crafted Pizza with Quality Ingredients.</text>
  </g>
  <g class="base-side base-side--right">
    <rect class="print-area" x="586" y="975" width="29" height="343"/>
    <text class="copy-bold" font-size="10.5" text-anchor="middle" dominant-baseline="middle"
          transform="translate(600.5,1146) rotate(-90)">You"ll miss 100% of the Pizza you don't eat.</text>
  </g>

  <!-- Front wall -->
  <g class="front-wall">
    <rect class="print-area" x="203" y="1362" width="343" height="30"/>
    <text class="copy-bold" x="375" y="1378" font-size="16" text-anchor="middle" dominant-baseline="middle">Get Your GAME ON!</text>
  </g>
</svg>
</body>
</html>
```